Buch-/eBook-Cover für Liebesroman
Zielgruppe
Ich bin Autorin und suche ein Cover für mein neues Buch. Meine Zielgruppe sind junge Erwachsene, die Liebesromane lesen.
Aufgabenstellung
Der Titel ist 'Als ob ein Regen durch die Stille fällt' und als Autorin soll Margarete Hollweck draufstehen.
Ich mag Cover, auf denen keine Menschen bzw. nicht der komplette Mensch zu sehen ist. Farbentechnisch würde ich mich überraschen lassen, solange es nicht zu bunt wird. :-) Als Schriftart darf es gern eine Schreibschrift sein. Ich lasse mich aber auch zu etwas anderem überreden, wenn es zum restlichen Cover passt. ;-)
Das Cover sollte eine Auflösung von mind. 300 dpi haben (gern mehr) und möglichst im jpg-Format sein.
Der Inhalt des Buches: Es geht um ein Männerpaar. Der eine ist verheiratet (mit einer Frau) und verliebt sich in seinen Kumpel. Die beiden beginnen eine Affäre, woraus aber bald mehr wird. Am Ende trennt er sich von seiner Frau und entscheidet sich für seinen Kumpel.
Es ist ein Liebesroman, aber das Cover sollte trotzdem nicht zu klischeehaft sein.
Da ich das hier nicht anders auswählen kann, noch eine kleine Anmerkung. Ich möchte nach Möglichkeit keine Stockmaterialien im Cover haben.

```html
<!DOCTYPE html>
<html lang="de">
<head>
<meta charset="utf-8">
<title>Als ob ein Regen durch die Stille fällt – Margarete Hollweck</title>
<link rel="stylesheet" href="https://fonts.googleapis.com/css2?family=Cinzel:wght@500;600&family=Great+Vibes&family=Montserrat:wght@400&family=Playfair+Display:ital,wght@1,600&display=swap">
<style>
  :root {
    --page-bg: #e9eaea;
    --sky-top: #6f7db4;
    --sky-mid: #a49bcb;
    --sky-rose: #dcb1c9;
    --horizon: #f6dccb;
    --sea-light: #a9c6c6;
    --sea-deep: #5f8597;
    --title-plum: #4b2a4e;
    --silhouette: 24, 20, 28;
    --white: #ffffff;
  }
  * { margin: 0; padding: 0; box-sizing: border-box; }
  html, body {
    width: 1000px;
    height: 1200px;
    overflow: hidden;
    background: var(--page-bg);
  }
  .cover {
    position: absolute;
    left: 50px;
    top: 35px;
    width: 900px;
    height: 1130px;
    overflow: hidden;
    box-shadow: 0 6px 18px rgba(0, 0, 0, 0.18);
  }
  .cover-art {
    position: absolute;
    inset: 0;
    background: linear-gradient(
      to bottom,
      var(--sky-top) 0%,
      var(--sky-mid) 30%,
      var(--sky-rose) 55%,
      var(--horizon) 75%,
      var(--sea-light) 76.5%,
      var(--sea-deep) 100%
    );
  }
  .couple-silhouette {
    position: absolute;
    left: 190px;
    top: 500px;
    width: 560px;
    height: 630px;
    background: radial-gradient(
      ellipse 50% 90% at 50% 100%,
      rgba(var(--silhouette), 0.92) 0%,
      rgba(var(--silhouette), 0.82) 55%,
      rgba(var(--silhouette), 0.35) 80%,
      rgba(var(--silhouette), 0) 100%
    );
  }
  .author {
    position: absolute;
    top: 58px;
    width: 100%;
    text-align: center;
    font-family: "Montserrat", sans-serif;
    font-weight: 400;
    font-size: 34px;
    letter-spacing: 2px;
    color: var(--white);
    text-transform: uppercase;
  }
  .title {
    position: absolute;
    top: 180px;
    width: 100%;
    text-align: center;
    color: var(--title-plum);
  }
  .title-caps {
    display: block;
    font-family: "Cinzel", serif;
    font-weight: 600;
    font-size: 70px;
    line-height: 1.1;
    font-variant: small-caps;
  }
  .title-caps.long { font-size: 60px; }
  .title-script {
    display: block;
    font-family: "Great Vibes", cursive;
    font-size: 140px;
    line-height: 1.05;
    margin: -8px 0 -6px;
  }
  .genre {
    position: absolute;
    bottom: 50px;
    width: 100%;
    text-align: center;
    font-family: "Playfair Display", serif;
    font-style: italic;
    font-weight: 600;
    font-size: 40px;
    color: var(--white);
  }
</style>
</head>
<body>
  <main class="cover">
    <div class="cover-art" role="img" aria-label="Abendhimmel in Violett und Rosa mit Sternen über dem ruhigen Meer"></div>
    <div class="couple-silhouette" role="img" aria-label="Silhouette zweier Männer, die sich vor dem Meer küssen"></div>
    <p class="author">Margarete Hollweck</p>
    <h1 class="title">
      <span class="title-caps">Als ob ein</span>
      <span class="title-script">Regen</span>
      <span class="title-caps long">durch die Stille fällt</span>
    </h1>
    <p class="genre">Roman</p>
  </main>
</body>
</html>
```